An image to show that our fees are offset by our good management

We work in the property sector.
We'd like a slide showing that our fees weigh very little compared with the savings we can generate if we do our job properly as property managers.
To do this, we've come up with a slide with a scale showing our fees on the left (which weigh less or the same) than the items on the right.
On the right you can see:
Savings on building maintenance costs
Savings on running costs
Optimization of vacant periods
Good monitoring of disputes to avoid rental losses
We welcome any other ideas you may have to highlight this concept (even off-balance sheet).

```html
<!DOCTYPE html>
<html lang="en">
<head>
<meta charset="utf-8">
<title>Our fees versus the savings of good management</title>
<link href="https://fonts.googleapis.com/css2?family=Questrial&display=swap" rel="stylesheet">
<style>
  :root {
    --bg: #ffffff;
    --beam-top: #9a9a9a;
    --beam-front: #333333;
    --stone-dark: #5a3114;
    --stone-mid: #7a4519;
    --stone-light: #a8845d;
    --label: #ffffff;
    --label-shadow: rgba(30, 15, 5, 0.75);
    --figure-a: #4a4a4a;
    --figure-b: #e0a62a;
  }
  html, body {
    margin: 0;
    padding: 0;
    width: 1200px;
    height: 675px;
    overflow: hidden;
    background: var(--bg);
  }
  .slide {
    position: relative;
    width: 1200px;
    height: 675px;
    background: var(--bg);
  }
  .scene {
    position: absolute;
    inset: 0;
  }
  .stone-label {
    font-family: "Questrial", "Century Gothic", sans-serif;
    fill: var(--label);
    text-anchor: middle;
    filter: url(#label-shadow);
  }
  .manager-figure {
    position: absolute;
    left: 162px;
    top: 218px;
    width: 140px;
    height: 166px;
    border-radius: 40px 40px 30px 30px;
    background: linear-gradient(160deg, var(--figure-a) 0%, #6b6b6b 60%, var(--figure-b) 100%);
    opacity: 0.85;
  }
</style>
</head>
<body>
<main class="slide">
  <svg class="scene" width="1200" height="675" viewBox="0 0 1200 675" xmlns="http://www.w3.org/2000/svg">
    <defs>
      <radialGradient id="stone-fill" cx="0.45" cy="0.4" r="0.75">
        <stop offset="0" stop-color="var(--stone-dark)"/>
        <stop offset="0.55" stop-color="var(--stone-mid)"/>
        <stop offset="1" stop-color="var(--stone-light)"/>
      </radialGradient>
      <linearGradient id="house-fill" x1="0" y1="0" x2="1" y2="1">
        <stop offset="0" stop-color="#8a5a30"/>
        <stop offset="0.5" stop-color="#7a4519"/>
        <stop offset="1" stop-color="#a8845d"/>
      </linearGradient>
      <filter id="label-shadow" x="-10%" y="-30%" width="120%" height="160%">
        <feDropShadow dx="1" dy="1.5" stdDeviation="1" flood-color="var(--label-shadow)"/>
      </filter>
    </defs>

    <!-- fulcrum house -->
    <g class="fulcrum">
      <polygon points="530,523 592,470 654,523 654,603 530,603" fill="url(#house-fill)"/>
      <polygon points="511,537 592,462 673,537 654,537 592,481 530,537" fill="#3e220d"/>
      <rect x="575" y="557" width="34" height="46" fill="var(--bg)"/>
    </g>

    <!-- beam -->
    <g class="beam">
      <polygon points="170,438 189,429 992,427 1012,436" fill="var(--beam-top)"/>
      <rect x="170" y="436" width="842" height="16" fill="var(--beam-front)"/>
      <circle cx="592" cy="443" r="16" fill="var(--bg)" stroke="var(--beam-front)" stroke-width="9"/>
    </g>

    <!-- fee stone -->
    <g class="stone stone-fees">
      <ellipse cx="278" cy="403" rx="73" ry="29" fill="url(#stone-fill)"/>
      <text class="stone-label" x="278" y="411" font-size="22">Our Fees</text>
    </g>

    <!-- savings stack -->
    <g class="stone stone-vacancy">
      <ellipse cx="868" cy="382" rx="118" ry="47" fill="url(#stone-fill)" transform="rotate(-2 868 382)"/>
      <text class="stone-label" x="868" y="385" font-size="19">Optimization of vacant</text>
      <text class="stone-label" x="868" y="407" font-size="19">periods</text>
    </g>
    <g class="stone stone-maintenance">
      <ellipse cx="870" cy="295" rx="103" ry="42" fill="url(#stone-fill)" transform="rotate(-4 870 295)"/>
      <text class="stone-label" x="871" y="295" font-size="17">Savings on building</text>
      <text class="stone-label" x="871" y="315" font-size="17">maintenance costs</text>
    </g>
    <g class="stone stone-disputes">
      <ellipse cx="852" cy="216" rx="88" ry="45" fill="url(#stone-fill)" transform="rotate(3 852 216)"/>
      <text class="stone-label" x="854" y="206" font-size="15.5">Good monitoring</text>
      <text class="stone-label" x="854" y="224" font-size="15.5">of disputes to avoid</text>
      <text class="stone-label" x="854" y="242" font-size="15.5">rental losses</text>
    </g>
    <g class="stone stone-running">
      <ellipse cx="854" cy="131" rx="74" ry="42" fill="url(#stone-fill)" transform="rotate(8 854 131)"/>
      <text class="stone-label" x="852" y="128" font-size="15.5">Savings on</text>
      <text class="stone-label" x="852" y="145" font-size="15.5">running costs</text>
    </g>
  </svg>

  <div class="manager-figure" role="img" aria-label="Illustration of a property manager in a suit balancing on a gold dollar coin"></div>
</main>
</body>
</html>
```